New Creative Busines Card

Hi Lead Designer,

How are you going?

I was hoping you can help me design the perfect business card for my new business. I have listed below some background information about the business and the concept to help with your design. I'm open to any form of creative ideas, but would like to have two types of colour schemes one dark color and one light.

I would like to have a dark set of design and a light (One design with one in black or dark background and one with light background to compare the contrast since the business card will be double sided one) I imagine this will be pretty easy to change the background of the design. Would prefer one side to have all the details and the other will just have a amazing logo (K7) to give it the finishing touch.

Feel free to email me if you have any questions.

Business Structure and design concepts:

Name of the business: K7 Advisory
Business: Dating agency and event management (Date night etc)
Concept: The main focus will be the K7 ( As some sort of a heart shape like logo) be creative
Details to include in the card will be general details like Name, Title: , Email, mobile, website (Contact details will be given later).

The rest of the idea is up to you, feel free to go crazy with your creative ideas.

Thank you for your help in advance, may the best candidate win~!

Target Market(s)

Target market will be Professional, Elegant, young and ambitious people.

Industry/Entity Type

Business

Requirements
Must have
• Focus on the K7 (as some sort of a heart shape logo). Since this is a double sides design would prefer on one side to focus on the just the K7 logo and the other side with a smaller version of the logo (with it or without) and all the details such as Name, Title, Mobile, Email, Website. Please have the design in landscape format.Not fuss with the Font as long as it is easy to read.
Nice to have
• Different Contrast in colours (keep it simple) one side dark colour scheme and one side light. Prefer to have 3-4 colours (not overwhelm with too many colours) to keep it simple and elegant.
Should not have
• Too colours, main focus is should be the K7 logo not the colours

```html
<!DOCTYPE html>
<html lang="en">
<head>
<meta charset="utf-8">
<title>K7 Advisory – Business Card</title>
<link rel="stylesheet" href="https://fonts.googleapis.com/css2?family=Open+Sans:ital,wght@0,400;1,700&display=swap">
<style>
  :root{
    --stage:#d6d6d6;
    --paper:#ffffff;
    --plum:#8a0a8c;
    --plum-light:#960096;
    --plum-deep:#5e0060;
    --aqua:#22c6d2;
    --mist:#ecd9ec;
    --snow:#ffffff;
  }
  *{margin:0;padding:0;box-sizing:border-box}
  html,body{width:975px;height:1200px;overflow:hidden}
  body{background:var(--stage);position:relative;font-family:"Open Sans",sans-serif}

  .card{position:absolute;left:34px;width:908px;overflow:hidden}
  .card--front{top:36px;height:561px;background:var(--paper)}
  .card--back{top:601px;height:562px;background:linear-gradient(180deg,var(--plum-light) 0%,var(--plum-deep) 100%)}

  .front__monogram{position:absolute;left:330px;top:-60px;font-size:600px;font-weight:400;line-height:1;color:var(--mist);letter-spacing:-10px;user-select:none;z-index:0}

  .holder__name,.holder__rule,.holder__title,.contacts{z-index:1}
  .holder__name{position:absolute;left:151px;top:182px;font-size:30px;font-weight:700;font-style:italic;color:var(--aqua);line-height:1}
  .holder__rule{position:absolute;left:123px;top:226px;width:394px;height:3px;background:var(--plum)}
  .holder__title{position:absolute;left:153px;top:240px;font-size:28px;color:var(--plum);line-height:1.2}

  .contacts{position:absolute;left:140px;top:328px;list-style:none}
  .contacts__item{display:flex;align-items:center;height:43px;font-size:20.5px;color:var(--aqua)}
  .contacts__icon{width:34px;height:26px;margin-right:14px;flex:none}

  .back__name{position:absolute;left:0;right:0;top:90px;text-align:center;font-size:300px;font-weight:400;line-height:1;letter-spacing:-10px;color:var(--snow)}
  .back__wordmark{position:absolute;left:0;right:0;top:380px;text-align:center;font-size:42px;font-weight:400;letter-spacing:0.55em;padding-left:0.55em;color:var(--aqua);line-height:1}
</style>
</head>
<body>
  <section class="card card--front">
    <div class="front__monogram" aria-hidden="true">K7</div>

    <p class="holder__name">Name</p>
    <div class="holder__rule"></div>
    <p class="holder__title">Title</p>

    <ul class="contacts">
      <li class="contacts__item">
        <svg class="contacts__icon" viewBox="0 0 34 26" aria-hidden="true"><path d="M14 3 q6 0 6 4 l-3 1 q-1-2-3-2z M14 23 q6 0 6-4 l-3-1 q-1 2-3 2z M16 7 q-3 6 0 12" fill="none" stroke="var(--plum)" stroke-width="3" stroke-linecap="round"/></svg>
        +(000) 1234 5678
      </li>
      <li class="contacts__item">
        <svg class="contacts__icon" viewBox="0 0 34 26" aria-hidden="true"><g fill="none" stroke="var(--plum)" stroke-width="1.6"><rect x="9" y="1" width="14" height="11"/><path d="M12 5h8M12 8h8"/><rect x="4" y="12" width="24" height="12"/><path d="M8 18h16"/></g></svg>
        name@emailaddress.com
      </li>
      <li class="contacts__item">
        <svg class="contacts__icon" viewBox="0 0 34 26" aria-hidden="true"><path d="M16 25 L8 12 A8 8 0 1 1 24 12 Z" fill="var(--plum)"/><circle cx="16" cy="9" r="3.2" fill="#fff"/></svg>
        your address, address 1
      </li>
      <li class="contacts__item">
        <svg class="contacts__icon" viewBox="0 0 34 26" aria-hidden="true"><g fill="none" stroke="var(--plum)" stroke-width="1.5"><circle cx="16" cy="13" r="11"/><ellipse cx="16" cy="13" rx="5" ry="11"/><path d="M5 13h22M7 7h18M7 19h18M16 2v22"/></g></svg>
        www.website.com
      </li>
    </ul>
  </section>

  <section class="card card--back">
    <p class="back__name">K7</p>
    <p class="back__wordmark">ADVISORY</p>
  </section>
</body>
</html>
```